New Business Card Design Project

The legal name of the company is TTTolvane, we also refer to it as simply Tolvane or you could also use the initials TTT...... please feel creative.
Excellent design.
On the second side, if you could image North and South America on each drop of water ... it almost looks like that now.
The website is www.tttolvane.com
Attached is another card with the required information; no addresses.

Industry/Entity Type

Legal

```html
<!DOCTYPE html>
<html lang="en">
<head>
<meta charset="utf-8">
<title>TTTolvane Business Card</title>
<link href="https://fonts.googleapis.com/css2?family=Cabin:wght@400;500&family=Oswald:wght@300&display=swap" rel="stylesheet">
<style>
  :root {
    --stage: #ececee;
    --front-bg: #1e1f33;
    --band: #1b3a78;
    --back-light: #1f4290;
    --back-dark: #22297a;
    --accent: #3fa9f5;
    --globe-light: #6fb4ec;
    --globe-dark: #2a66b8;
    --white: #ffffff;
  }
  * { margin: 0; padding: 0; box-sizing: border-box; }
  html, body { width: 1200px; height: 800px; overflow: hidden; }
  body {
    background: var(--stage);
    font-family: "Cabin", "Gill Sans", sans-serif;
    color: var(--white);
    position: relative;
  }
  .card {
    position: absolute;
    top: 221px;
    width: 525px;
    height: 291px;
    overflow: hidden;
  }
  .card--front { left: 56px; background: var(--front-bg); }
  .card--back {
    left: 619px;
    background: linear-gradient(100deg, var(--back-light) 0%, var(--back-light) 35%, var(--back-dark) 100%);
  }

  .globe-area {
    position: absolute;
    left: 296px; top: 28px;
    width: 210px; height: 137px;
    background: radial-gradient(ellipse at 45% 55%, var(--globe-light) 0%, var(--globe-dark) 60%, rgba(42, 102, 184, 0) 100%);
  }

  .front-band {
    position: absolute;
    left: 0; top: 165px;
    width: 100%; height: 85px;
    background: var(--band);
  }
  .brand {
    position: absolute;
    left: 29px; top: 17px;
    display: flex; align-items: center; gap: 12px;
  }
  .brand__dot {
    width: 56px; height: 56px; border-radius: 50%;
    background: var(--white);
  }
  .brand__name {
    font-family: "Oswald", "Arial Narrow", sans-serif;
    font-weight: 300;
    font-size: 44px;
    letter-spacing: 0.5px;
    line-height: 1;
  }
  .front-band__web {
    position: absolute;
    left: 309px; top: 51px;
    font-size: 17px; letter-spacing: 0.3px;
  }

  .person { position: absolute; left: 44px; top: 116px; }
  .person__name { font-size: 29px; color: var(--accent); line-height: 1.1; }
  .person__role { font-size: 16px; margin-top: 8px; letter-spacing: 0.2px; }

  .company { position: absolute; left: 243px; top: 52px; }
  .company__name { font-size: 33px; letter-spacing: 0.8px; line-height: 1.05; }
  .company__legal { font-size: 31px; line-height: 1.6; letter-spacing: 0.3px; }
  .contact { list-style: none; margin-top: 12px; font-size: 13px; line-height: 25px; }
</style>
</head>
<body>

<section class="card card--front" aria-label="Card front">
  <div class="globe-area" role="img" aria-label="Globe illustration with a light flare"></div>
  <div class="front-band">
    <div class="brand">
      <span class="brand__dot" aria-hidden="true"></span>
      <span class="brand__name">TOLVANE</span>
    </div>
    <span class="front-band__web">www.tttolvane.com</span>
  </div>
</section>

<section class="card card--back" aria-label="Card back">
  <div class="person">
    <p class="person__name">Leo Danvers</p>
    <p class="person__role">Managing Director</p>
  </div>
  <div class="company">
    <p class="company__name">TOLVANE</p>
    <p class="company__legal">tttolvane sa, llc</p>
    <ul class="contact">
      <li>USA: +1 (555) 014 2200</li>
      <li>Guatemala: +502 5550 0148</li>
      <li>ldv@tttolvane.com</li>
    </ul>
  </div>
</section>

</body>
</html>
```